Training program workbook Cover & Insert

We need a cover for a training manual for a Management and leadership program & the first topic title page.

We are an executive consultation business that develops training programs and provides in-house strategic support for businesses across different sectors. We see this will be an ongoing design project as we will be creating a cover for the folder (to be inserted into the A4 binder) and then as we develop the sections a series of title pages for each topic.
We are currently looking for designs for the Main cover and first topic ( 2 x A4 pages / like a double sided flyer really). The designs should reflect
- sophistication
- growth
- drive
- fun
- agility
With a theme that can be replicated across a series of topics e.g. communication, time effectiveness, conflict resolution etc etc

The Program is called "PIVOT".
The tagline for the binder cover is
"Creating Leadership Agility in a Changing World"

The first topic is "TIME"
Tagline
Living & Working in "REAL" Time

We are open to any colour other than orange.

Target Market(s)

Training Program participants

Industry/Entity Type

Training

Font styles to use
Serif

Colors

Designer to choose colors to be used in the design.

Requirements
Must have
• A design framework that can be expanded for various topic cover pages within the manual.
• Eye Catching graphics that excite the viewer and entice them to continue reading
Nice to have
• Copyright (symbol) Marlowe Group in small font at the bottom of the page
Should not have
• Typical daggy old school training images

```html
<!DOCTYPE html>
<html lang="en">
<head>
<meta charset="utf-8">
<title>PIVOT Workbook – Cover &amp; TIME Topic Page</title>
<link href="https://fonts.googleapis.com/css2?family=Jost:wght@300;400;600&display=swap" rel="stylesheet">
<style>
  :root {
    --ink: #3d4654;
    --ink-soft: #7a7f88;
    --slate: #3b4350;
    --grey: #7b7b7d;
    --grey-light: #9a9a9c;
    --red: #d42a2a;
    --red-deep: #b81f24;
    --red-warm: #e5482f;
    --green: #8cc63f;
    --teal: #1fa98a;
    --blue: #52b6e6;
    --yellow: #f2b233;
    --rule: #6d6a86;
    --paper: #ffffff;
    --frame: #8a8a8a;
  }
  * { margin: 0; padding: 0; box-sizing: border-box; }
  html, body { width: 1200px; height: 787px; overflow: hidden; background: var(--paper); }
  body { position: relative; font-family: "Jost", sans-serif; color: var(--ink); }

  .page {
    position: absolute; top: 0; height: 787px;
    border: 1px solid var(--frame); background: var(--paper); overflow: hidden;
  }
  .page--cover { left: 0; width: 557px; border-left: none; }
  .page--topic { left: 643px; width: 557px; border-right: none; }

  .page-art { position: absolute; inset: 0; width: 100%; height: 100%; }

  .title {
    position: absolute; font-weight: 300; line-height: 1; color: var(--ink);
    white-space: nowrap;
  }
  .title--cover { right: 40px; top: 42px; font-size: 132px; letter-spacing: 6px; }
  .title--topic { right: 40px; top: 24px; font-size: 104px; letter-spacing: 8px; }

  .colour-bar { position: absolute; height: 4px; display: flex; }
  .colour-bar span { flex: 1; }
  .colour-bar .green { background: var(--green); }
  .colour-bar .teal { background: var(--teal); }
  .colour-bar .blue { background: var(--blue); }
  .colour-bar .yellow { background: var(--yellow); }
  .colour-bar .dark { background: var(--ink); }
  .page--cover .colour-bar { left: 128px; width: 387px; top: 171px; }
  .page--topic .colour-bar { left: 199px; width: 316px; top: 126px; }

  .tagline { position: absolute; color: var(--ink-soft); white-space: nowrap; font-weight: 400; }
  .tagline--cover { left: 130px; top: 178px; font-size: 16px; letter-spacing: 1.1px; }
  .tagline--topic { right: 40px; top: 136px; font-size: 18.5px; letter-spacing: 1.4px; }

  .footer-rule { position: absolute; top: 663px; right: 0; height: 1px; background: var(--rule); }
  .page--cover .footer-rule { width: 240px; }
  .page--topic .footer-rule { width: 240px; }

  .tick-mark { position: absolute; left: 27px; top: 703px; width: 10px; height: 1px; background: var(--ink); }

  .copyright {
    position: absolute; right: 24px; top: 738px;
    font-size: 15px; font-weight: 600; color: var(--ink); white-space: nowrap; letter-spacing: 0.2px;
  }
</style>
</head>
<body>

<section class="page page--cover" aria-label="PIVOT programme cover">
  <svg class="page-art" viewBox="0 0 557 787" aria-hidden="false">
    <defs>
      <linearGradient id="cover-red" x1="0" y1="0" x2="1" y2="1">
        <stop offset="0" stop-color="var(--red-deep)"/>
        <stop offset="0.55" stop-color="var(--red)"/>
        <stop offset="1" stop-color="var(--red-warm)"/>
      </linearGradient>
      <linearGradient id="cover-grey" x1="0" y1="0" x2="1" y2="0">
        <stop offset="0" stop-color="#8a8a8c"/>
        <stop offset="1" stop-color="#5e5f63"/>
      </linearGradient>
    </defs>
    <polygon class="facet facet--slate" points="0,222 103,325 0,428" fill="var(--slate)"/>
    <polygon class="facet facet--grey" points="0,444 103,548 0,652" fill="url(#cover-grey)"/>
    <g class="diamond diamond--upper">
      <polygon points="226,290 226,434 154,362" fill="var(--grey)"/>
      <polygon points="226,290 298,362 226,434" fill="var(--slate)"/>
    </g>
    <g class="diamond diamond--lower">
      <polygon points="226,440 226,584 154,512" fill="var(--slate)"/>
      <polygon points="226,440 298,512 226,584" fill="var(--grey)"/>
    </g>
    <polygon role="img" aria-label="Red low-poly faceted diamond" points="113,333 216,436 113,539 10,436" fill="url(#cover-red)"/>
    <polygon role="img" aria-label="Small red low-poly faceted diamond" points="305,369 373,437 305,505 237,437" fill="url(#cover-red)"/>
  </svg>

  <h1 class="title title--cover">PIVOT</h1>
  <div class="colour-bar"><span class="green"></span><span class="teal"></span><span class="blue"></span><span class="yellow"></span><span class="dark"></span></div>
  <p class="tagline tagline--cover">Creating Leadership Agility in a Changing World</p>

  <div class="footer-rule"></div>
  <div class="tick-mark"></div>
  <p class="copyright">© Marlowe Group</p>
</section>

<section class="page page--topic" aria-label="TIME topic title page">
  <svg class="page-art" viewBox="643 0 557 787">
    <defs>
      <linearGradient id="office-blur" x1="0" y1="0" x2="0" y2="1">
        <stop offset="0" stop-color="#bfe0f2"/>
        <stop offset="0.3" stop-color="#e6d9c4"/>
        <stop offset="0.55" stop-color="#d9a56a"/>
        <stop offset="0.8" stop-color="#8a7a6e"/>
        <stop offset="1" stop-color="#c9c6c0"/>
      </linearGradient>
      <linearGradient id="topic-red" x1="0" y1="0" x2="1" y2="1">
        <stop offset="0" stop-color="var(--red-deep)"/>
        <stop offset="0.55" stop-color="var(--red)"/>
        <stop offset="1" stop-color="var(--red-warm)"/>
      </linearGradient>
    </defs>

    <polygon role="img" aria-label="Blurred office interior photograph"
      points="843,258 998,258 1078,338 1078,493 998,573 843,573 765,493 765,338" fill="url(#office-blur)"/>

    <g class="facets" stroke="var(--paper)" stroke-width="2">
      <polygon points="843,258 998,258 921,336" fill="var(--grey)"/>
      <polygon points="843,573 998,573 921,496" fill="var(--grey)"/>
      <polygon points="765,338 842,415 765,493" fill="var(--slate)"/>
      <polygon points="1078,338 1000,415 1078,493" fill="var(--slate)"/>
      <polygon role="img" aria-label="Red low-poly faceted diamond" points="921,337 999,415 921,493 843,415" fill="url(#topic-red)"/>
    </g>

    <g class="icon icon--team" fill="var(--paper)">
      <circle cx="920" cy="273" r="5"/>
      <rect x="912" y="280" width="16" height="12" rx="4"/>
      <circle cx="905" cy="277" r="4"/>
      <rect x="898" y="283" width="12" height="9" rx="3"/>
      <circle cx="935" cy="277" r="4"/>
      <rect x="930" y="283" width="12" height="9" rx="3"/>
    </g>
    <g class="icon icon--search" stroke="var(--paper)" fill="none" stroke-width="3">
      <circle cx="790" cy="405" r="9"/>
      <line x1="797" y1="412" x2="808" y2="423" stroke-width="4" stroke-linecap="round"/>
    </g>
    <g class="icon icon--chart" fill="var(--paper)">
      <rect x="1033" y="414" width="6" height="8"/>
      <rect x="1042" y="408" width="6" height="14"/>
      <rect x="1051" y="401" width="6" height="21"/>
      <rect x="1060" y="394" width="6" height="28"/>
    </g>
    <g class="icon icon--gears" fill="none" stroke="var(--paper)">
      <circle cx="912" cy="547" r="7" stroke-width="6" stroke-dasharray="3 2.5"/>
      <circle cx="912" cy="547" r="3" stroke-width="2"/>
      <circle cx="933" cy="538" r="5" stroke-width="4.5" stroke-dasharray="2.5 2"/>
      <circle cx="933" cy="538" r="2" stroke-width="1.5"/>
    </g>
  </svg>

  <h2 class="title title--topic">TIME</h2>
  <div class="colour-bar"><span class="green"></span><span class="teal"></span><span class="blue"></span><span class="yellow"></span><span class="dark"></span></div>
  <p class="tagline tagline--topic">Living &amp; Working in "REAL" Time</p>

  <div class="footer-rule"></div>
  <p class="copyright">© Marlowe Group</p>
</section>

</body>
</html>
```